Vantor Roving Car Wash and Detail Services, 'needs a logo and card design'

I need a logo and Card design for a new company based in Perth Western Australia called, 'Vantor Roving Car Wash and Detail Services'. I want to offer a mobile car wash and detail service across all the Perth metropolitan areas at lower prices, and offer more reliability. I would like to see designs with colours such as red, white, and black. The final design should communicate trust reliability and confidence in the services I can provide. The card must include my first name 'Oswin' and my mobile number '0471208356' for an obligation free quote.
Updates

Target Market(s)

Aimed at anyone who owns and drives a motor vehicle.

Industry/Entity Type

It Company

Contact Information for Business Card

Business Name'Vantor Roving Car Wash and Detail Services', My first name 'Oswin', and my mobile phone '0471208356' for an obligation free quote.

Font styles to use
Serif
Decorative
Script

Colors
ffffff
000000
d3d3d3
ec1f27
7f7f7f

Requirements
Must have
• Business Name'Vantor Roving Car Wash and Detail Services', My first name 'Oswin', and my mobile phone '0471208356' for an obligation free quote.
• Logo design
Nice to have
• A slogan, such as 'I come to you, and wash your car wherever you are' to let customers know I am at their service.
• Car design 'shine and clean feeling'

```html
<!DOCTYPE html>
<html lang="en">
<head>
<meta charset="utf-8">
<title>Vantor Roving Car Wash and Detail Services – Business Card</title>
<link href="https://fonts.googleapis.com/css2?family=Exo+2:wght@600;700;800&family=Orbitron:wght@700&family=Lato:wght@400;700&display=swap" rel="stylesheet">
<style>
  :root {
    --page-bg: #d3d3d3;
    --card-top-a: #f4f2f0;
    --card-top-b: #dcdad8;
    --black: #000000;
    --red: #ec1f27;
    --red-deep: #b3121a;
    --red-dark: #7a0a0f;
    --white: #ffffff;
    --grey: #7f7f7f;
    --ink: #1a1a1a;
  }
  * { box-sizing: border-box; margin: 0; padding: 0; }
  html, body {
    width: 1200px; height: 970px; overflow: hidden;
    background: var(--page-bg);
  }
  .canvas {
    position: relative; width: 1200px; height: 970px;
    display: flex; align-items: center; justify-content: center;
  }
  .card {
    position: relative; width: 1040px; height: 592px;
    display: flex; flex-direction: column;
    box-shadow: 0 20px 50px rgba(0,0,0,0.25);
    overflow: hidden;
  }
  .card__brand {
    height: 306px;
    background: linear-gradient(180deg, var(--card-top-a) 0%, var(--card-top-b) 100%);
    display: flex; flex-direction: column; align-items: center; justify-content: center;
    padding-top: 60px;
  }
  .brand-name {
    font-family: "Exo 2", sans-serif; font-weight: 800;
    color: var(--red-deep); text-align: center; text-transform: uppercase;
    line-height: 1.1;
  }
  .brand-name__main { display: block; font-size: 62px; letter-spacing: 2px; }
  .brand-name__sub { display: block; font-size: 25px; letter-spacing: 1.5px; margin-top: 4px; }
  .card__contact {
    height: 226px; background: var(--black);
    display: flex; flex-direction: column; align-items: center;
    padding-top: 42px;
  }
  .contact-name {
    font-family: "Orbitron", sans-serif; font-weight: 700;
    font-size: 50px; color: var(--red); letter-spacing: 1px; line-height: 1;
  }
  .contact-lines { margin-top: 22px; text-align: center; }
  .contact-line {
    font-family: "Exo 2", sans-serif; font-weight: 700;
    font-size: 25px; line-height: 32px; color: var(--white);
  }
  .contact-line__label { color: var(--red); }
  .contact-line__value { color: #d9d2cf; }
  .card__slogan {
    height: 60px;
    background: linear-gradient(90deg, var(--red-deep) 0%, var(--red) 30%, var(--red-dark) 60%, var(--red) 85%, var(--red-deep) 100%);
    display: flex; align-items: center; justify-content: center;
  }
  .slogan {
    font-family: "Lato", sans-serif; font-weight: 400;
    font-size: 27px; color: var(--ink);
  }
</style>
</head>
<body>
  <main class="canvas">
    <section class="card" aria-label="Business card">
      <header class="card__brand">
        <h1 class="brand-name">
          <span class="brand-name__main">Vantor Roving</span>
          <span class="brand-name__sub">Car Wash and Detail Services</span>
        </h1>
      </header>
      <div class="card__contact">
        <p class="contact-name">Oswin</p>
        <div class="contact-lines">
          <p class="contact-line"><span class="contact-line__label">Mobile:</span> <span class="contact-line__value">0471208356</span></p>
          <p class="contact-line"><span class="contact-line__label">Email:</span> <span class="contact-line__value">info@vantorroving com</span></p>
        </div>
      </div>
      <footer class="card__slogan">
        <p class="slogan">I come to you, and wash your car wherever you are</p>
      </footer>
    </section>
  </main>
</body>
</html>
```